Nutrivo, site for appointments between nutritionists and patients

Nutrivo is a platform for connecting nutritionists and patients with appointment scheduling and online payment.

We like teal, but we're not fixated on it.

The site must be simple, accessible and pleasant and dynamic and evoke the joy of nutrition while not forgetting the health aspect.

Example of illustration which tend towards what we are looking for.

Logo and graphic charter

Home page, simple little information

1)
Book a physical or video consultation with a dietitian (medirova, so calm now, léna, vistam)

2)
Reason for using Nutrivo

Access state-certified nutrition experts with several years of training (registration of professionals on the site only with adeli number and valid diploma)

Access the availability of tens of thousands of healthcare professionals.

Make an appointment online, 24/7, for a physical or video consultation.

Secure personal data

3)
You are a dietitian nutritionist

Use nutrivo to optimize your activity
Free up time by making an appointment online
Limit unfulfilled appointments with online payment
Take advantage of Nutrivo's notoriety to obtain better visibility
Use a commercial platform to develop your patient base
Use the platform's communication tools
Etc ...

Page 2 if applicable

List of professionals

Page 3 if search by specific name

Name photo
The essentials, map and access information, presentation, timetables, prices, site, make an appointment

Page 3 bis more in-depth presentation.

Page 4
agenda appointment booking page

Payment page

Professional page

Page 1
presentation of assets

Page 2 limited access

Rates with bronze, silver, gold, platinum account

Products, training and services page for sale

Blog page

Nutrivo is a platform that connects nutritionists and patients with online appointments and payment.

We like the teal color but we are not set on it.

The site must be simple, accessible, pleasant and dynamic and evoke the joy of nutrition while not forgetting the health aspect.

Example of illustrations that tend towards what we are looking for.

Our Logo is on the attachment

Home page

1)
Book a physical or video consultation with a dietician (ex site: medirova, so calm now, léna, vistam)

2)
Reasons to use Nutrivo

Access to experts in nutrition with several years of training (registration of professionals on the site only with adeli number and valid diploma)

Access the availability of tens of thousands of dieticians.

Secure personal data

3) You are a dietitian nutritionist

Free up time with online appointment booking
Limit the number of missed appointments thanks to online payment
Take advantage of Nutrivo's notoriety to get a better visibility
Use the communication tools of the platform
Etc ...

Page 2 if the patient don't choose a professional and put only a place.

List of professionals

Page 3 if searching by specific name

Photo name
The essentials, map and access information, presentation, opening hours, rates, site, make an appointment

Page 3 bis - more detailed presentation of dietician.

Page 4
diary page for making an appointment

Payment page

Blog page

Side Professional page

Page 1
presentation of assets

Page 2 (limited access)

Page 3

Products, training and services for sale page

Target Market(s)

The general public

Number of Pages Required

5+ page

Colors
00AB8E
00BBA5
67D7C9
C6EFE9
E9F9F6

Requirements
Must have
• Read the project in the attached documents. Read the project on the attachments
Should not have
• No photographs

```html
<!DOCTYPE html>
<html lang="en">
<head>
<meta charset="utf-8">
<title>Nutrivo – Find a nutritionist</title>
<link rel="stylesheet" href="https://fonts.googleapis.com/css2?family=Lexend:wght@300;400&family=Roboto:wght@400;500;700&display=swap">
<style>
:root{
  --teal-deep:#179b80;
  --teal:#1fa98c;
  --teal-mid:#35bea5;
  --teal-light:#5fd0c0;
  --teal-pale:#c6efe9;
  --mint:#e9f9f6;
  --grey-band:#f0f1f3;
  --ink:#1e1e1e;
  --muted:#555a5e;
  --footer:#26272b;
  --white:#ffffff;
}
*{box-sizing:border-box;margin:0;padding:0}
html,body{width:1200px;height:2488px;overflow:hidden}
body{position:relative;background:var(--white);font-family:"Roboto",sans-serif;color:var(--ink)}
.abs{position:absolute}
.display{font-family:"Lexend",sans-serif;font-weight:300}

/* hero */
.hero-bg{left:0;top:0;width:1200px;height:700px}
.brand{left:111px;top:31px;height:34px;display:flex;align-items:center;gap:8px;color:var(--white);font-weight:500;font-size:27px;line-height:34px}
.brand-dot{width:14px;height:14px;border-radius:50%;background:var(--white)}
.nav{left:337px;top:39px;display:flex;gap:29px;color:var(--white);font-weight:700;font-size:14px;line-height:18px}
.login{left:934px;top:39px;display:flex;align-items:center;gap:14px;color:var(--white);font-weight:700;font-size:14px;line-height:18px}
.hero-title{left:109px;top:224px;color:var(--white);font-size:38px;line-height:43px}
.hero-text{left:111px;top:374px;width:478px;color:var(--white);font-weight:700;font-size:13.5px;line-height:21px}
.search{left:111px;top:438px;width:499px;height:50px;background:var(--white);border:2px solid var(--white);display:flex;font-size:11px;color:#444}
.search .field{display:flex;align-items:center;gap:10px;padding-left:12px}
.search .name{width:160px;border-right:1px solid #ddd}
.search .where{width:199px;justify-content:space-between;padding-right:12px}
.search .where span{display:flex;align-items:center;gap:10px}
.search .go{flex:1;background:var(--teal-light);color:var(--white);font-weight:700;font-size:14px;display:flex;align-items:center;justify-content:center}
.art{display:block}

/* reasons */
.section-title{width:1200px;left:0;text-align:center;font-size:30px;color:var(--ink)}
.reason{top:854px;width:200px;text-align:center;font-weight:700;font-size:14px;line-height:21.5px}
.reason .badge{width:100px;height:100px;margin:0 auto 20px;border-radius:50%;background:var(--teal-light);display:flex;align-items:center;justify-content:center}
.reason .badge span{width:84px;height:84px;border-radius:50%;background:var(--teal);display:flex;align-items:center;justify-content:center}
.divider{top:864px;width:1px;height:158px;background:#dcdcdc}

/* professional */
.pro-title{left:651px;top:1248px;font-size:30px}
.ticks{left:651px;top:1310px;list-style:none;font-size:14px;color:#444}
.ticks li{height:30px;display:flex;align-items:center;gap:18px}
.btn{height:47px;display:flex;align-items:center;justify-content:center;color:var(--white);font-weight:700;font-size:14px;border-radius:2px}
.btn-dark{background:var(--teal)}
.btn-light{background:var(--teal-light)}

/* appointment */
.appt-text{left:300px;top:1836px;width:600px;text-align:center;font-size:16px;line-height:23px;color:var(--muted)}

/* footer */
.foot-bg{left:0;top:2040px;width:1200px;height:390px}
.foot-h{top:2182px;color:var(--white);font-weight:700;font-size:14px;text-decoration:underline;text-underline-offset:3px}
.foot-about{left:113px;top:2224px;width:280px;color:#e3e3e3;font-size:14.5px;line-height:26px}
.socials{left:113px;top:2321px;display:flex;gap:12px}
.socials span{width:30px;height:30px;border-radius:50%;border:1px solid #cfcfcf;display:flex;align-items:center;justify-content:center}
.socials span i{width:8px;height:8px;border-radius:50%;background:#cfcfcf}
.contact{left:443px;color:#e8e8e8;font-size:14.5px;line-height:22px;display:flex;align-items:center;gap:18px}
.contact .ring{width:38px;height:38px;border-radius:50%;border:1px solid #cfcfcf;display:flex;align-items:center;justify-content:center;flex:none}
.links{list-style:none;color:#e8e8e8;font-size:14.5px}
.links li{height:32px;display:flex;align-items:center;gap:12px}
.links li b{font-weight:400;font-size:12px;color:#fff}
.bottom{left:0;top:2426px;width:1200px;height:62px;background:var(--teal);color:var(--white);font-size:15px;display:flex;align-items:center;justify-content:space-between;padding:0 115px 0 111px}
.cards{display:flex;gap:4px}
.cards span{width:30px;height:22px;border-radius:2px;background:var(--white)}
.cards span:nth-child(2){background:#f1f1f1}
</style>
</head>
<body>

<!-- hero -->
<svg class="abs hero-bg" viewBox="0 0 1200 700" aria-hidden="true">
  <defs>
    <linearGradient id="heroGrad" x1="0" y1="0" x2="0" y2="1">
      <stop offset="0" stop-color="#1a9e85"/>
      <stop offset="1" stop-color="#46c8b2"/>
    </linearGradient>
  </defs>
  <path d="M0 0H1200V628C1130 668 1060 694 980 692C880 690 800 652 700 648C590 644 520 668 420 660C330 652 300 612 230 612C130 612 60 640 0 664Z" fill="url(#heroGrad)"/>
</svg>

<div class="abs brand"><span class="brand-dot"></span>nutrivo</div>

<nav class="abs nav"><span>HOME</span><span>ABOUT US</span><span>REASONS TO USE NUTRIVO</span><span>DIETITIAN NUTRITIONIST</span></nav>
<div class="abs login">
  <svg width="18" height="18" viewBox="0 0 18 18" aria-hidden="true"><circle cx="9" cy="9" r="8.5" fill="#fff"/><circle cx="9" cy="7" r="3" fill="#1fa98c"/><path d="M3.5 14.5C5 11.5 13 11.5 14.5 14.5" stroke="#1fa98c" stroke-width="2" fill="none"/></svg>
  LOGIN / REGISTER
</div>

<h1 class="abs hero-title display">Find a healthcare<br>professional &amp; make<br>an appointment online!</h1>
<p class="abs hero-text">Lorem ipsum dolor sit amet, consectetur adipiscing elit, sed do eiusmod tempor incididunt ut labore et dolore magna aliqua.</p>

<div class="abs search">
  <div class="field name">
    <svg width="10" height="10" viewBox="0 0 10 10" aria-hidden="true"><circle cx="4" cy="4" r="3" stroke="#333" stroke-width="1.6" fill="none"/><path d="M6.3 6.3L9 9" stroke="#333" stroke-width="1.8"/></svg>
    Name , Establishment
  </div>
  <div class="field where">
    <span><svg width="8" height="11" viewBox="0 0 8 11" aria-hidden="true"><path d="M4 11C1 7 0 5.5 0 4a4 4 0 0 1 8 0c0 1.5-1 3-4 7z" fill="#333"/><circle cx="4" cy="4" r="1.4" fill="#fff"/></svg>Where</span>
    <svg width="12" height="12" viewBox="0 0 12 12" aria-hidden="true"><circle cx="6" cy="6" r="3.5" stroke="#333" stroke-width="1.4" fill="none"/><circle cx="6" cy="6" r="1.2" fill="#333"/><path d="M6 0v2.5M6 9.5V12M0 6h2.5M9.5 6H12" stroke="#333" stroke-width="1.4"/></svg>
  </div>
  <div class="go">TO RESEARCH</div>
</div>

<svg class="abs art" style="left:645px;top:179px" width="522" height="399" viewBox="0 0 522 399" role="img" aria-label="Illustration of people around a large bathroom scale, a diet plan clipboard, a treadmill, measuring tape and fresh vegetables">
  <defs>
    <linearGradient id="heroArt" x1="0" y1="0" x2="1" y2="1">
      <stop offset="0" stop-color="#f8f1e6"/>
      <stop offset="0.55" stop-color="#f4e4d2"/>
      <stop offset="1" stop-color="#efd3bf"/>
    </linearGradient>
  </defs>
  <path d="M70 40C130 10 210 30 270 40C340 50 400 0 460 20C520 45 525 130 505 190C490 240 470 300 420 345C370 395 280 405 210 380C150 360 100 330 60 280C20 230 0 170 10 120C18 80 40 55 70 40Z" fill="url(#heroArt)"/>
</svg>

<!-- reasons -->
<h2 class="abs section-title display" style="top:758px">Reasons to use Nutrivo</h2>

<div class="abs reason" style="left:130px">
  <div class="badge"><span><svg width="44" height="44" viewBox="0 0 44 44" aria-hidden="true"><rect x="6" y="6" width="24" height="32" rx="2" fill="#fff"/><rect x="13" y="3" width="10" height="6" rx="1" fill="#fff" stroke="#1fa98c" stroke-width="1.5"/><path d="M11 16h14M11 22h14M11 28h8" stroke="#1fa98c" stroke-width="2"/><circle cx="32" cy="32" r="8" fill="#fff" stroke="#1fa98c" stroke-width="1.5"/></svg></span></div>
  Access to experts in nutrition with several years of training
</div>
<div class="abs divider" style="left:362px"></div>
<div class="abs reason" style="left:383px">
  <div class="badge"><span><svg width="44" height="44" viewBox="0 0 44 44" aria-hidden="true"><circle cx="22" cy="24" r="15" fill="#fff"/><path d="M8 24h28" stroke="#1fa98c" stroke-width="2"/><path d="M12 26v5M16 26v4M20 26v5M24 26v4M28 26v5M32 26v4" stroke="#1fa98c" stroke-width="1.5"/><path d="M22 9c0-3 2-5 4-5" stroke="#fff" stroke-width="2" fill="none"/></svg></span></div>
  Access the availability of tens of thousands of dieticians.
</div>
<div class="abs divider" style="left:601px"></div>
<div class="abs reason" style="left:636px">
  <div class="badge"><span><svg width="44" height="44" viewBox="0 0 44 44" aria-hidden="true"><rect x="8" y="8" width="22" height="30" rx="2" fill="#fff"/><rect x="14" y="5" width="10" height="6" rx="1" fill="#fff" stroke="#1fa98c" stroke-width="1.5"/><path d="M12 18h14M12 24h10M12 30h8" stroke="#1fa98c" stroke-width="2"/><circle cx="31" cy="31" r="7" fill="#fff" stroke="#1fa98c" stroke-width="1.5"/></svg></span></div>
  Make an appointment online 24/7, for a physical or video consultation.
</div>
<div class="abs divider" style="left:871px"></div>
<div class="abs reason" style="left:889px">
  <div class="badge"><span><svg width="44" height="44" viewBox="0 0 44 44" aria-hidden="true"><ellipse cx="19" cy="11" rx="11" ry="4" fill="#fff"/><path d="M8 15c0 2.2 5 4 11 4s11-1.8 11-4v5c0 2.2-5 4-11 4S8 22.2 8 20z" fill="#fff"/><path d="M8 24c0 2.2 5 4 11 4v6c-6 0-11-1.8-11-4z" fill="#fff"/><circle cx="31" cy="31" r="8" fill="#fff" stroke="#1fa98c" stroke-width="1.5"/><path d="M27 31l3 3 5-6" stroke="#1fa98c" stroke-width="2" fill="none"/></svg></span></div>
  Secure personal data
</div>

<!-- professional band -->
<svg class="abs" style="left:0;top:1090px" width="1200" height="610" viewBox="0 0 1200 610" aria-hidden="true">
  <path d="M0 66C80 30 160 0 240 6C330 14 400 58 520 60C650 62 700 16 820 30C960 46 1020 92 1100 86C1150 82 1180 60 1200 42V530C1130 580 1060 600 980 596C880 590 800 550 680 548C560 546 500 568 400 560C300 552 250 500 170 500C100 500 40 530 0 560Z" fill="var(--grey-band)"/>
</svg>

<svg class="abs art" style="left:109px;top:1228px" width="463" height="353" viewBox="0 0 463 353" role="img" aria-label="Illustration of a heart with a pulse line, vitamin bubbles, pill bottles, vegetables and small people">
  <defs>
    <linearGradient id="proArt" x1="0" y1="0" x2="1" y2="1">
      <stop offset="0" stop-color="#f7ece0"/>
      <stop offset="0.6" stop-color="#f3e0cc"/>
      <stop offset="1" stop-color="#eed4bf"/>
    </linearGradient>
  </defs>
  <path d="M60 30C120 0 200 15 260 10C330 4 410 20 445 70C470 110 455 170 440 220C420 285 370 335 290 348C210 360 140 345 90 305C40 265 5 210 2 150C0 100 20 55 60 30Z" fill="url(#proArt)"/>
</svg>

<h2 class="abs pro-title display">You are a dietitian nutritionist</h2>
<ul class="abs ticks">
  <li><svg width="12" height="12" viewBox="0 0 12 12" aria-hidden="true"><circle cx="6" cy="6" r="6" fill="var(--teal)"/><path d="M3.2 6.2l2 2 3.6-4" stroke="#fff" stroke-width="1.6" fill="none"/></svg>Use nutrivo to optimize your activity</li>
  <li><svg width="12" height="12" viewBox="0 0 12 12" aria-hidden="true"><circle cx="6" cy="6" r="6" fill="var(--teal)"/><path d="M3.2 6.2l2 2 3.6-4" stroke="#fff" stroke-width="1.6" fill="none"/></svg>Free up time with online appointment booking</li>
  <li><svg width="12" height="12" viewBox="0 0 12 12" aria-hidden="true"><circle cx="6" cy="6" r="6" fill="var(--teal)"/><path d="M3.2 6.2l2 2 3.6-4" stroke="#fff" stroke-width="1.6" fill="none"/></svg>Limit the number of missed appointments thanks to online payment</li>
  <li><svg width="12" height="12" viewBox="0 0 12 12" aria-hidden="true"><circle cx="6" cy="6" r="6" fill="var(--teal)"/><path d="M3.2 6.2l2 2 3.6-4" stroke="#fff" stroke-width="1.6" fill="none"/></svg>Take advantage of Nutrivo's notoriety to get a better visibility</li>
  <li><svg width="12" height="12" viewBox="0 0 12 12" aria-hidden="true"><circle cx="6" cy="6" r="6" fill="var(--teal)"/><path d="M3.2 6.2l2 2 3.6-4" stroke="#fff" stroke-width="1.6" fill="none"/></svg>Use a commercial platform to develop your patient base</li>
  <li><svg width="12" height="12" viewBox="0 0 12 12" aria-hidden="true"><circle cx="6" cy="6" r="6" fill="var(--teal)"/><path d="M3.2 6.2l2 2 3.6-4" stroke="#fff" stroke-width="1.6" fill="none"/></svg>Use the communication tools of the platform</li>
</ul>
<div class="abs btn btn-dark" style="left:651px;top:1516px;width:161px">BOOK A PHYSICAL</div>
<div class="abs btn btn-light" style="left:831px;top:1516px;width:178px">VIDEO CONSULTATION</div>

<!-- appointment -->
<svg class="abs art" style="left:99px;top:1776px" width="241" height="184" viewBox="0 0 241 184" role="img" aria-label="Illustration of a woman stretching beside a phone showing a diet plan, with fruit">
  <defs>
    <linearGradient id="apptLeft" x1="0" y1="0" x2="1" y2="1">
      <stop offset="0" stop-color="#eef6f1"/>
      <stop offset="1" stop-color="#e2efe7"/>
    </linearGradient>
  </defs>
  <path d="M40 40C70 10 110 20 150 30C200 42 240 70 238 115C236 160 190 182 130 182C70 182 20 168 6 130C-6 95 15 62 40 40Z" fill="url(#apptLeft)"/>
</svg>
<svg class="abs art" style="left:886px;top:1776px" width="236" height="194" viewBox="0 0 236 194" role="img" aria-label="Illustration of two people beside a diet plan clipboard and vegetables">
  <defs>
    <linearGradient id="apptRight" x1="0" y1="0" x2="1" y2="1">
      <stop offset="0" stop-color="#f8efe4"/>
      <stop offset="1" stop-color="#f0d8c3"/>
    </linearGradient>
  </defs>
  <path d="M60 15C100 -5 160 5 200 30C232 52 240 100 225 140C208 180 160 196 110 190C60 184 15 160 5 115C-4 75 25 32 60 15Z" fill="url(#apptRight)"/>
</svg>
<h2 class="abs section-title display" style="top:1778px">Making an Appointment</h2>
<p class="abs appt-text">Sed ut perspiciatis unde omnis iste natus error sit voluptatem accusantium doloremque laudantium, totam rem aperiam, eaque ipsa quae ab illo inventore veritatis et quasi architecto beatae vitae dicta sunt explicabo</p>
<div class="abs btn btn-dark" style="left:520px;top:1925px;width:160px">BOOK A PHYSICAL</div>

<!-- footer -->
<svg class="abs foot-bg" viewBox="0 0 1200 390" aria-hidden="true">
  <path d="M0 68C70 40 130 8 210 8C300 8 370 46 470 80C560 108 640 84 760 70C880 56 960 104 1060 96C1130 90 1170 60 1200 44V390H0Z" fill="var(--footer)"/>
</svg>

<h3 class="abs foot-h" style="left:113px">ABOUT US</h3>
<p class="abs foot-about">Ut enim ad minima veniam, quis nostrum exercitationem ullam corporis suscipit laboriosam, nisi ut aliquid.</p>
<div class="abs socials"><span><i></i></span><span><i></i></span><span><i></i></span><span><i></i></span></div>

<h3 class="abs foot-h" style="left:443px">CONTACT US</h3>
<div class="abs contact" style="top:2226px">
  <span class="ring"><svg width="11" height="15" viewBox="0 0 8 11" aria-hidden="true"><path d="M4 11C1 7 0 5.5 0 4a4 4 0 0 1 8 0c0 1.5-1 3-4 7z" fill="none" stroke="#e8e8e8" stroke-width="1"/><circle cx="4" cy="4" r="1.4" fill="#e8e8e8"/></svg></span>
  <span>47 Larkfield Avenue<br>Brandon, MB - R7A 2K9</span>
</div>
<div class="abs contact" style="top:2290px">
  <span class="ring"><svg width="14" height="11" viewBox="0 0 14 11" aria-hidden="true"><rect x=".6" y=".6" width="12.8" height="9.8" rx="1.5" fill="none" stroke="#e8e8e8" stroke-width="1.2"/><path d="M1 1.5l6 4.5 6-4.5" stroke="#e8e8e8" stroke-width="1.2" fill="none"/></svg></span>
  <span>info@nutrivo.com</span>
</div>
<div class="abs contact" style="top:2345px;font-weight:700;font-size:17px">
  <span class="ring"><svg width="13" height="13" viewBox="0 0 13 13" aria-hidden="true"><path d="M2.5 0.5l2.2 2.6-1.2 1.6c.8 1.9 2.4 3.5 4.3 4.3l1.6-1.2 2.6 2.2-1.3 2.2C5 11.5 1 7.6.3 1.8z" fill="#e8e8e8"/></svg></span>
  <span>1 800 555 0142</span>
</div>

<h3 class="abs foot-h" style="left:728px">QUICK LINKS</h3>
<ul class="abs links" style="left:728px;top:2212px">
  <li><b>»</b>Home</li><li><b>»</b>About Us</li><li><b>»</b>Reasons to use Nutrivo</li><li><b>»</b>dietitian nutritionist</li><li><b>»</b>Latest Blog</li>
</ul>

<h3 class="abs foot-h" style="left:951px">OTHER LINKS</h3>
<ul class="abs links" style="left:951px;top:2212px">
  <li><b>»</b>Contact Us</li><li><b>»</b>FAQ</li><li><b>»</b>Help Service</li><li><b>»</b>Terms Of Use</li><li><b>»</b>Privacy Policy</li>
</ul>

<div class="abs bottom">
  <span>© 2021 Nutrivo. All Rights Reserved</span>
  <span class="cards" aria-label="Accepted payment cards"><span></span><span></span><span></span><span></span></span>
</div>

</body>
</html>
```